Lakeview Optiquip Partners Post Card

Lakeview Optiquip Partners. We buy, sell and service ophthalmic equipment for the eye care professional.
We sell New and Pre-Owned Chairs and Stands, Slit Lamps, Refractors, , Autolensometers, Perimeters, Autrefractor/Keratometer, Retinal Cameras and many more.
We also do a equipment repair, preventive maintenance, practice relocation and set-up and in-office service calls.

Target Market(s)

Opthalmologists, optometrist and all eye care professionals.

Industry/Entity Type

Medical Equipment

Font styles to use
Sans Serif

Colors
0355a3
33a6d7

Requirements
Must have
• My web site address: www.lakeviewoptiquip.example, tel. 555-718-4096, email: lakeviewlens@mailbox.example.
• I will mail the postcard, i need space for the postage and recipient address on the back.
Nice to have
• https://www.sketchhive.example/design/20472615
• https://www.sketchhive.example/design/20472608
• https://www.sketchhive.example/design/20439751

```html
<!DOCTYPE html>
<html lang="en">
<head>
<meta charset="utf-8">
<title>Lakeview Optiquip Partners Post Card</title>
<link rel="stylesheet" href="https://fonts.googleapis.com/css2?family=Open+Sans:wght@400;600;700;800&display=swap">
<style>
  :root{
    --brand-blue:#0355a3;
    --brand-sky:#33a6d7;
    --ink:#3a3f47;
    --panel-grey:#eceef1;
    --panel-grey-dark:#d5d9de;
    --paper:#ffffff;
    --page:#e9eaec;
    --line:#9aa0a8;
  }
  *{box-sizing:border-box;margin:0;padding:0}
  html,body{width:689px;height:1200px;overflow:hidden}
  body{background:var(--page);font-family:"Open Sans",Arial,sans-serif;color:var(--ink);position:relative}
  .postcard{position:absolute;left:34px;width:620px;height:400px;background:var(--paper);overflow:hidden;box-shadow:0 6px 16px rgba(0,0,0,.25)}
  .postcard--front{top:170px}
  .postcard--back{top:630px}
  .abs{position:absolute}
  .on-top{z-index:2}

  /* front */
  .brand-panel{left:0;top:0;width:330px;height:105px;background:linear-gradient(90deg,var(--panel-grey-dark),var(--panel-grey) 60%,#fafbfc)}
  .brand-name{font-weight:700;color:var(--brand-blue);font-size:14px;letter-spacing:.3px;display:flex;align-items:center;gap:7px;line-height:18px}
  .brand-name .mark{flex:none;width:9px;height:9px;background:var(--brand-blue)}
  .front-brand{left:40px;top:44px}
  .shapes{left:0;top:0}
  .headline{right:14px;top:17px;color:#fff;text-align:right}
  .headline h2{font-size:22px;font-weight:700;line-height:1.1}
  .headline p{font-size:13.5px;font-weight:600;margin-top:6px;display:flex;align-items:center;gap:6px;justify-content:flex-end}
  .headline p::before,.headline p::after{content:"";height:1px;background:#fff;width:48px}
  .headline p::after{width:30px}
  .photo{background:linear-gradient(135deg,#e8eef5 0%,#8fb3d8 40%,#2d5e96 70%,#9cc3e6 100%)}
  .front-photo{left:265px;top:92px;width:355px;height:212px}
  .sell-title{left:12px;top:116px;font-size:23px;line-height:24px;color:var(--ink);white-space:nowrap}
  .sell-title b{color:var(--brand-blue);font-weight:800}
  .sell-title b.sky{color:var(--brand-sky)}
  .ticks{list-style:none}
  .ticks li{display:flex;align-items:flex-start;gap:7px;font-size:11.3px;line-height:16.2px}
  .ticks svg{flex:none;margin-top:3px}
  .sell-list{left:14px;top:172px;width:180px}
  .chair{left:200px;top:172px;width:58px;height:126px;background:linear-gradient(180deg,#f4f5f7,#c9ced6 50%,#2f3238)}
  .thumb{width:70px;height:58px;background:linear-gradient(160deg,#ffffff,#d8dde4);box-shadow:0 1px 3px rgba(0,0,0,.3);transform:skewX(-8deg)}
  .contact{left:398px;top:316px;width:214px}
  .phone{display:flex;align-items:center;gap:6px;font-size:26px;font-weight:700;color:var(--brand-blue);line-height:30px}
  .contact-row{display:flex;align-items:center;gap:6px;font-size:11.5px;line-height:19px;margin-left:2px;white-space:nowrap}
  .contact-row b{color:var(--brand-blue);font-weight:700}
  .contact-row.small{font-size:10.5px}

  /* back */
  .back-top{left:0;top:0;width:340px;height:101px;background:var(--panel-grey)}
  .also-title{left:20px;top:10px;font-size:23px;color:var(--ink)}
  .also-title b{color:var(--brand-blue);font-weight:800}
  .also-text{left:20px;top:40px;width:300px;font-size:11.3px;line-height:16px}
  .services-title{left:20px;top:108px;color:#fff;font-size:22px;padding-bottom:3px;border-bottom:1px solid #fff}
  .services-title b{font-weight:700}
  .service-list{left:20px;top:143px;width:240px;color:#fff}
  .service-list li{margin-bottom:5.5px}
  .slitlamp{left:258px;top:112px;width:52px;height:150px;background:linear-gradient(180deg,#f7f8fa,#c4cad3)}
  .back-brand{left:362px;top:50px;width:130px;font-size:13px}
  .stamp{left:501px;top:17px;width:92px;height:84px;border:1px solid #555}
  .address-line{left:360px;width:233px;height:1px;background:var(--line)}
</style>
</head>
<body>

<section class="postcard postcard--front" aria-label="Postcard front">
  <div class="abs brand-panel"></div>
  <svg class="abs shapes" width="620" height="400" viewBox="0 0 620 400" aria-hidden="true">
    <polygon points="322,0 620,0 620,92 276,92" fill="var(--brand-blue)"/>
    <polygon points="300,0 314,0 266,105 252,105" fill="var(--brand-sky)"/>
    <polygon points="0,302 430,302 395,400 0,400" fill="var(--brand-blue)"/>
    <polygon points="430,302 620,302 620,400 395,400" fill="var(--panel-grey)"/>
  </svg>
  <div class="abs brand-name front-brand"><span class="mark"></span>Lakeview Optiquip Partners</div>
  <div class="abs headline">
    <h2>We buy, sell and service</h2>
    <p>Ophthalmic Equipment</p>
  </div>
  <div class="abs photo front-photo" role="img" aria-label="Close-up photo of slit lamp eyepieces in a bright clinic"></div>

  <div class="abs chair" role="img" aria-label="Product photo of an exam chair and stand"></div>
  <div class="abs sell-title on-top">WE <b>SELL NEW</b><br>and <b class="sky">PRE-OWNED</b></div>
  <ul class="abs ticks sell-list on-top">
    <li><svg width="9" height="9" viewBox="0 0 10 10"><circle cx="5" cy="5" r="4.3" fill="none" stroke="var(--brand-sky)" stroke-width="1.2"/><path d="M3 5.2l1.4 1.4L7 3.8" fill="none" stroke="var(--brand-sky)" stroke-width="1.2"/></svg>Chairs and Stands</li>
    <li><svg width="9" height="9" viewBox="0 0 10 10"><circle cx="5" cy="5" r="4.3" fill="none" stroke="var(--brand-sky)" stroke-width="1.2"/><path d="M3 5.2l1.4 1.4L7 3.8" fill="none" stroke="var(--brand-sky)" stroke-width="1.2"/></svg>Slit Lamps</li>
    <li><svg width="9" height="9" viewBox="0 0 10 10"><circle cx="5" cy="5" r="4.3" fill="none" stroke="var(--brand-sky)" stroke-width="1.2"/><path d="M3 5.2l1.4 1.4L7 3.8" fill="none" stroke="var(--brand-sky)" stroke-width="1.2"/></svg>Refractors</li>
    <li><svg width="9" height="9" viewBox="0 0 10 10"><circle cx="5" cy="5" r="4.3" fill="none" stroke="var(--brand-sky)" stroke-width="1.2"/><path d="M3 5.2l1.4 1.4L7 3.8" fill="none" stroke="var(--brand-sky)" stroke-width="1.2"/></svg>Autolensometers</li>
    <li><svg width="9" height="9" viewBox="0 0 10 10"><circle cx="5" cy="5" r="4.3" fill="none" stroke="var(--brand-sky)" stroke-width="1.2"/><path d="M3 5.2l1.4 1.4L7 3.8" fill="none" stroke="var(--brand-sky)" stroke-width="1.2"/></svg>Perimeters</li>
    <li><svg width="9" height="9" viewBox="0 0 10 10"><circle cx="5" cy="5" r="4.3" fill="none" stroke="var(--brand-sky)" stroke-width="1.2"/><path d="M3 5.2l1.4 1.4L7 3.8" fill="none" stroke="var(--brand-sky)" stroke-width="1.2"/></svg>Autrefractor/Keratometer</li>
    <li><svg width="9" height="9" viewBox="0 0 10 10"><circle cx="5" cy="5" r="4.3" fill="none" stroke="var(--brand-sky)" stroke-width="1.2"/><path d="M3 5.2l1.4 1.4L7 3.8" fill="none" stroke="var(--brand-sky)" stroke-width="1.2"/></svg><span>Retinal Cameras and<br>many more</span></li>
  </ul>

  <div class="abs thumb" style="left:16px;top:318px" role="img" aria-label="Product photo of an autorefractor"></div>
  <div class="abs thumb" style="left:102px;top:318px" role="img" aria-label="Product photo of a lensometer"></div>
  <div class="abs thumb" style="left:188px;top:318px" role="img" aria-label="Product photo of a phoropter"></div>
  <div class="abs thumb" style="left:274px;top:318px" role="img" aria-label="Product photo of a perimeter"></div>

  <div class="abs contact">
    <div class="phone"><svg width="16" height="16" viewBox="0 0 16 16" aria-hidden="true"><path d="M4 1.5l2.2 2.8-1.3 1.8c.9 2 2.5 3.6 4.5 4.5l1.8-1.3 2.8 2.2-1.4 2.2C7.6 14.5 1.5 8.4 1.8 3z" fill="none" stroke="var(--ink)" stroke-width="1.3"/></svg>555-718-4096</div>
    <div class="contact-row"><svg width="12" height="12" viewBox="0 0 12 12" aria-hidden="true"><circle cx="6" cy="6" r="5.6" fill="var(--ink)"/><rect x="3" y="4" width="6" height="4" fill="none" stroke="#fff" stroke-width=".8"/><path d="M3 4l3 2.2L9 4" fill="none" stroke="#fff" stroke-width=".8"/></svg><span><b>lakeviewlens</b>@mailbox.example</span></div>
    <div class="contact-row small"><svg width="12" height="12" viewBox="0 0 12 12" aria-hidden="true"><circle cx="6" cy="6" r="5.6" fill="var(--ink)"/><circle cx="6" cy="6" r="3.2" fill="none" stroke="#fff" stroke-width=".7"/><path d="M2.8 6h6.4M6 2.8v6.4" stroke="#fff" stroke-width=".7"/></svg><span>www.<b>lakeviewoptiquip</b>.example</span></div>
  </div>
</section>

<section class="postcard postcard--back" aria-label="Postcard back">
  <div class="abs back-top"></div>
  <svg class="abs shapes" width="620" height="400" viewBox="0 0 620 400" aria-hidden="true">
    <polygon points="0,101 320,101 294,345 0,345" fill="var(--brand-blue)"/>
    <polygon points="252,101 320,101 294,345 240,345" fill="var(--brand-sky)" opacity=".45"/>
  </svg>
  <div class="abs also-title"><b>WE ALSO</b> DO</div>
  <p class="abs also-text">Equipment Repair, Preventive Maintenance,<br>Practice Relocation and Set-up and In-office<br>Service Calls.</p>

  <div class="abs slitlamp" role="img" aria-label="Product photo of a slit lamp in front of an eye chart"></div>
  <div class="abs services-title on-top">Our <b>Services</b></div>
  <ul class="abs ticks service-list on-top">
    <li><svg width="9" height="9" viewBox="0 0 10 10"><path d="M1.5 5.2l2.3 2.3L8.5 2.5" fill="none" stroke="#fff" stroke-width="1.4"/></svg>Full Service Department</li>
    <li><svg width="9" height="9" viewBox="0 0 10 10"><path d="M1.5 5.2l2.3 2.3L8.5 2.5" fill="none" stroke="#fff" stroke-width="1.4"/></svg>Repair and Maintenance</li>
    <li><svg width="9" height="9" viewBox="0 0 10 10"><path d="M1.5 5.2l2.3 2.3L8.5 2.5" fill="none" stroke="#fff" stroke-width="1.4"/></svg>In-Office Service Calls</li>
    <li><svg width="9" height="9" viewBox="0 0 10 10"><path d="M1.5 5.2l2.3 2.3L8.5 2.5" fill="none" stroke="#fff" stroke-width="1.4"/></svg><span>Chairs and Stands,<br>Lane Maintenance and Urgent Repairs</span></li>
    <li><svg width="9" height="9" viewBox="0 0 10 10"><path d="M1.5 5.2l2.3 2.3L8.5 2.5" fill="none" stroke="#fff" stroke-width="1.4"/></svg>Practice Moves andRelocation's</li>
  </ul>

  <div class="abs thumb" style="left:22px;top:275px" role="img" aria-label="Product photo of an autorefractor"></div>
  <div class="abs thumb" style="left:108px;top:275px" role="img" aria-label="Product photo of a lens edger"></div>
  <div class="abs thumb" style="left:194px;top:275px" role="img" aria-label="Product photo of a headband ophthalmoscope"></div>

  <div class="abs brand-name back-brand"><span class="mark"></span><span>Lakeview Optiquip<br>Partners</span></div>
  <div class="abs stamp"></div>
  <div class="abs address-line" style="top:225px"></div>
  <div class="abs address-line" style="top:271px"></div>
  <div class="abs address-line" style="top:319px"></div>
</section>

</body>
</html>
```